Natural Light/Organic/Documentary Photography Business

I like a simple, approachable, feminine, earthy/organic feel. Earth/neutral tones, nothing too loud or obnoxious. I like the watercolor look. I don't want anything too trendy or something I'll get tired of after a couple months. As far as colors, I am much more a fan of cream/taupe/blue/green...not a fan of pink or purple at all.

Target Market(s)

Weddings & Families

Industry/Entity Type

Wedding Photography

Contact Information for Business Card

website, email, phone number

Font styles to use
Other font styles liked:
• Horizontes, Gotham

Colors

Designer to choose colors to be used in the design.

Requirements
Must have
• Website: www.elspethmarlowe.com
• Phone: 412.638.9057
• Email: elspeth@elspethmarlowe.com
Nice to have
• I like the watercolor look but its not necessary. I like simple/earthy tones. Nothing too loud or distracting. Simple & feminine without being too girly. I like an approachable/soft feel.
• Instagram: www.instagram.com/elspethmarlowephotography/
Should not have
• NO loud colors or design or pattern. I do not want a photo of a camera or lens or anything cheesy like that.

```html
<!DOCTYPE html>
<html lang="en">
<head>
<meta charset="utf-8">
<title>Elspeth Marlowe Photography – Business Card</title>
<link href="https://fonts.googleapis.com/css2?family=Mrs+Saint+Delafield&family=Quicksand:wght@400&family=Montserrat:wght@400&display=swap" rel="stylesheet">
<style>
  :root {
    --page-bg: #ffffff;
    --card-bg: #f6f1e7;
    --card-edge: #8a8178;
    --ink: #6a6159;
    --wash-sage: #c3cfae;
    --wash-sage-soft: #dde3cc;
    --wash-green: #6f8270;
    --wash-green-soft: #94a391;
    --wash-blue: #9fb5be;
    --wash-blue-soft: #c4d2d6;
  }
  html, body {
    margin: 0;
    padding: 0;
    width: 1115px;
    height: 1200px;
    overflow: hidden;
    background: var(--page-bg);
  }
  .canvas {
    position: relative;
    width: 1115px;
    height: 1200px;
  }
  .business-card {
    position: absolute;
    left: 279px;
    top: 128px;
    width: 571px;
    height: 327px;
    box-sizing: border-box;
    border: 2px solid var(--card-edge);
    background: var(--card-bg);
    overflow: hidden;
  }
  .wash {
    position: absolute;
    opacity: 0.9;
  }
  .wash-sage {
    left: -14px;
    top: -8px;
    width: 285px;
    height: 312px;
    border-radius: 30% 55% 35% 45% / 22% 45% 50% 38%;
    background: radial-gradient(ellipse at 42% 45%, var(--wash-sage) 0%, var(--wash-sage-soft) 100%);
  }
  .wash-green {
    left: -10px;
    top: 205px;
    width: 70px;
    height: 130px;
    border-radius: 55% 45% 30% 20% / 40% 45% 30% 30%;
    background: radial-gradient(ellipse at 40% 50%, var(--wash-green) 0%, var(--wash-green-soft) 100%);
  }
  .wash-blue {
    left: 428px;
    top: 165px;
    width: 160px;
    height: 175px;
    border-radius: 45% 35% 20% 55% / 40% 30% 30% 50%;
    background: radial-gradient(ellipse at 60% 55%, var(--wash-blue) 0%, var(--wash-blue-soft) 100%);
  }
  .brand {
    position: absolute;
    left: 0;
    right: 0;
    top: 60px;
    text-align: center;
    color: var(--ink);
  }
  .brand-name {
    margin: 0;
    font-family: "Mrs Saint Delafield", cursive;
    font-weight: 400;
    font-size: 80px;
    line-height: 1;
    letter-spacing: 2px;
  }
  .brand-tagline {
    margin: -4px 0 0 10px;
    font-family: "Montserrat", sans-serif;
    font-size: 9.5px;
    letter-spacing: 10px;
    text-transform: uppercase;
  }
  .contact {
    position: absolute;
    left: 0;
    right: 0;
    top: 219px;
    margin: 0;
    padding: 0;
    list-style: none;
    text-align: center;
    font-family: "Quicksand", sans-serif;
    font-size: 19.5px;
    line-height: 28px;
    color: var(--ink);
  }
</style>
</head>
<body>
  <main class="canvas">
    <section class="business-card">
      <div class="wash wash-sage" role="img" aria-label="Soft sage watercolour leaf wash"></div>
      <div class="wash wash-green" role="img" aria-label="Deep green watercolour foliage wash"></div>
      <div class="wash wash-blue" role="img" aria-label="Dusty blue watercolour petal wash"></div>

      <header class="brand">
        <h1 class="brand-name">Elspeth Marlowe</h1>
        <p class="brand-tagline">Photography</p>
      </header>

      <ul class="contact">
        <li class="contact-phone">412.638.9057</li>
        <li class="contact-email">elspeth@elspethmarlowe.com</li>
        <li class="contact-web">www.elspethmarlowe.com</li>
      </ul>
    </section>
  </main>
</body>
</html>
```